Small Catering Menu

I am looking to make a small menu for catering for my company. I am thinking of a small A5 size booklet which will also have some pictures and the cover needs to be attractive.
Likely to be 8-12 pages depending upon your design (could be less or more). I need 2-3 pages as proposal concept (Cover, inside first page and one menu page) and if we like it we will make the project guaranteed before finishing the rest of the project to add security for the designer.
Pictures will be provided to the designer whose concept is the best as they are too heavy. But use generic photos for now (rather large ones) if possible.
Logo is available and so is the inside text as well as some other tidbits.
I will provide the fonts too to ensure it maintains the corporate integrity that we are following.
Catering

```html
<!DOCTYPE html>
<html lang="en">
<head>
<meta charset="utf-8">
<title>Harbor Table Catering – Menu</title>
<link rel="stylesheet" href="https://fonts.googleapis.com/css2?family=Source+Sans+3:wght@400;600;700&display=swap">
<style>
  :root {
    --red: #e24f45;
    --red-light: #ec6a60;
    --red-deep: #cc4331;
    --red-strip: #d24d3a;
    --night: #1f1516;
    --cocoa: #4a362f;
    --salmon: #f0806e;
    --white: #ffffff;
    --bread-1: #6b3a1c;
    --bread-2: #c07a3e;
    --cheese-1: #2a1a12;
    --cheese-2: #d9b860;
    --juice-1: #a8562a;
    --juice-2: #e69a48;
  }
  * { margin: 0; padding: 0; box-sizing: border-box; }
  html, body { width: 1200px; height: 858px; overflow: hidden; background: var(--night); }
  body { font-family: "Source Sans 3", Arial, sans-serif; color: var(--white); }

  .menu-sheet { position: relative; width: 1200px; height: 858px; overflow: hidden; background: var(--night); }

  .header-band { position: absolute; left: 0; top: 0; width: 1200px; height: 130px; background: var(--red); }
  .header-edge { position: absolute; left: 0; top: 130px; width: 1200px; height: 18px; background: var(--red-deep); }
  .header-flourish { position: absolute; left: 0; top: 0; width: 600px; height: 148px;
    background: radial-gradient(ellipse at 45% 45%, var(--red-light), rgba(226,79,69,0) 70%); }

  .brand-top { position: absolute; left: 876px; top: 10px; width: 250px; text-align: center;
    font-size: 24px; font-weight: 600; letter-spacing: 0.5px; line-height: 1.35; color: var(--white); }

  .section-title { position: absolute; left: 24px; font-size: 31px; font-weight: 400; line-height: 1; }
  .section-title .leader { font-size: 14px; letter-spacing: 1.6px; }

  .item-number { position: absolute; left: 30px; font-size: 40px; font-weight: 400; line-height: 1; }
  .item-number.accent { color: var(--salmon); }
  .item-name { position: absolute; font-size: 17px; font-weight: 600; line-height: 23px; }
  .item-desc { position: absolute; left: 88px; font-size: 13px; font-weight: 700; white-space: nowrap; }
  .item-leader { position: absolute; left: 476px; width: 185px; border-top: 2px dotted rgba(255,255,255,.75); }
  .item-price { position: absolute; left: 720px; font-size: 14px; font-weight: 700; }

  .photo-frame { position: absolute; left: 897px; width: 217px; background: var(--white); padding: 8px; }
  .photo-fill { width: 100%; height: 100%; }
  .photo-bread { background: radial-gradient(ellipse at 55% 55%, var(--bread-2), var(--bread-1) 75%); }
  .photo-cheese { background: radial-gradient(ellipse at 55% 60%, var(--cheese-2), var(--cheese-1) 70%); }
  .photo-juice { background: radial-gradient(ellipse at 50% 60%, var(--juice-2), var(--juice-1) 80%); }

  .footer-strip { position: absolute; left: 0; top: 675px; width: 1200px; height: 23px; background: var(--red-strip); }
  .footer-bar { position: absolute; left: 357px; top: 677px; width: 490px; height: 20px; background: var(--white); }
  .footer-band { position: absolute; left: 0; top: 698px; width: 1200px; height: 160px; background: var(--cocoa); }

  .tagline { position: absolute; left: 180px; top: 720px; font-size: 50px; font-weight: 400; line-height: 1.2; }
  .tagline-copy { position: absolute; left: 84px; top: 792px; width: 434px; text-align: center;
    font-size: 10px; font-weight: 700; line-height: 14px; }

  .brand-bottom { position: absolute; left: 900px; top: 738px; width: 210px; text-align: center; }
  .brand-mark { width: 44px; height: 44px; border-radius: 50%; background: var(--white); margin: 0 auto 10px; }
  .brand-bottom .brand-name { font-size: 20px; font-weight: 600; letter-spacing: 0.5px; line-height: 1.25; }
</style>
</head>
<body>
<main class="menu-sheet">
  <div class="header-band"></div>
  <div class="header-edge"></div>
  <div class="header-flourish" role="img" aria-label="Decorative flowing lines across the header"></div>

  <div class="brand-top">HARBOR TABLE<br>CATERING</div>

  <h2 class="section-title" style="top:152px">Appetizers<span class="leader">..........................</span></h2>

  <span class="item-number accent" style="top:221px">01</span>
  <span class="item-name" style="left:96px;top:219px">Dynamite Shrimps</span>
  <span class="item-desc" style="top:240px">your food item description, ingredients etc..</span>
  <span class="item-leader" style="top:256px"></span>
  <span class="item-price" style="top:247px">$4,5</span>

  <span class="item-number" style="top:329px">02</span>
  <span class="item-name" style="left:96px;top:328px">Tuna Fish Cutlets.</span>
  <span class="item-desc" style="top:348px">your food item description, ingredients etc.. goes here</span>
  <span class="item-leader" style="top:362px"></span>
  <span class="item-price" style="top:353px">$4,5</span>

  <h2 class="section-title" style="top:407px">Sandwiches<span class="leader">..........................</span></h2>

  <span class="item-number" style="top:491px">04</span>
  <span class="item-name" style="left:88px;top:489px">Tuna Sanwich</span>
  <span class="item-desc" style="top:511px">your food item description, ingredients etc.. goes here</span>
  <span class="item-leader" style="top:524px"></span>
  <span class="item-price" style="top:516px">$8.50</span>

  <span class="item-number accent" style="top:580px">05</span>
  <span class="item-name" style="left:88px;top:577px">Pan Fried Baja Fish Fillet in<br>Ciabatta Bread whith Cheese</span>
  <span class="item-desc" style="top:624px">your food item description...</span>
  <span class="item-leader" style="top:629px"></span>
  <span class="item-price" style="top:620px">$6.99</span>

  <div class="photo-frame" style="top:101px;height:145px"><div class="photo-fill photo-bread" role="img" aria-label="Photo of sweet bread loaves on a basket"></div></div>
  <div class="photo-frame" style="top:255px;height:143px"><div class="photo-fill photo-cheese" role="img" aria-label="Photo of assorted cheeses with cherry tomatoes"></div></div>
  <div class="photo-frame" style="top:408px;height:143px"><div class="photo-fill photo-juice" role="img" aria-label="Photo of fresh fruit juices in glasses and jugs"></div></div>

  <div class="footer-strip"></div>
  <div class="footer-bar"></div>
  <div class="footer-band"></div>

  <div class="photo-frame" style="top:563px;height:144px"><div class="photo-fill photo-bread" role="img" aria-label="Photo of sweet bread loaves on a basket"></div></div>

  <h1 class="tagline">By the sea</h1>
  <p class="tagline-copy">Vestibulum lacinia arcu eget nulla. Class aptent taciti sociosqu ad litora torquent per conubia nostra, per inceptos himenaeos. Curabitur sodales ligula in libero.</p>

  <div class="brand-bottom">
    <div class="brand-mark"></div>
    <div class="brand-name">HARBOR TABLE<br>CATERING</div>
  </div>
</main>
</body>
</html>
```